Product Label Design

Need a product design for our Epsom salt product, needs to have a luxurious simple feel to it. The picture attached is our brand and wordage on it, the bag we think should be a stand up bag that should be offwhite/creme color. The other picture are products that we like. We updated the packaging to be a Kraft tube box, please see the attached photo for dimensions.

```html
<!DOCTYPE html>
<html lang="en">
<head>
<meta charset="utf-8">
<title>RIVO Bright – Epsom Salt Tube Label</title>
<link rel="stylesheet" href="https://fonts.googleapis.com/css2?family=Archivo:wght@500;700;800&display=swap">
<style>
  :root {
    --page-bg: #ffffff;
    --wrap-bg: #f3f7f9;
    --band-edge: #89b1c5;
    --band-mid: #b4d1dd;
    --ink: #1c1c1c;
    --ink-soft: #4a4a4a;
    --label-white: #ffffff;
  }
  html, body {
    margin: 0;
    padding: 0;
    width: 1200px;
    height: 1200px;
    overflow: hidden;
    background: var(--page-bg);
  }
  .canvas {
    position: relative;
    width: 1200px;
    height: 1200px;
  }
  .label-wrap {
    position: absolute;
    left: 345px;
    top: 60px;
    width: 511px;
    height: 1078px;
    overflow: hidden;
  }
  .label-art {
    position: absolute;
    inset: 0;
  }
  .label-text {
    position: absolute;
    inset: 0;
    font-family: "Archivo", "Helvetica Neue", Arial, sans-serif;
    text-align: center;
  }
  .brand-name {
    position: absolute;
    left: 0;
    right: 0;
    top: 526px;
    margin: 0;
    font-size: 118px;
    font-weight: 800;
    line-height: 1;
    letter-spacing: -2px;
    color: var(--ink);
  }
  .variant-name {
    position: absolute;
    left: 0;
    right: 0;
    top: 652px;
    margin: 0;
    font-size: 42px;
    font-weight: 800;
    line-height: 1;
    letter-spacing: -1px;
    color: var(--label-white);
  }
  .ingredients {
    position: absolute;
    left: 0;
    right: 0;
    top: 704px;
    margin: 0;
    padding: 0;
    list-style: none;
    font-size: 15px;
    font-weight: 700;
    line-height: 22px;
    letter-spacing: -0.4px;
    color: var(--ink);
  }
  .ingredients .origin {
    color: var(--ink-soft);
    font-weight: 500;
  }
  .net-weight {
    position: absolute;
    left: 0;
    right: 0;
    top: 988px;
    margin: 0;
    font-size: 16px;
    font-weight: 500;
    letter-spacing: -0.4px;
    color: var(--ink-soft);
  }
</style>
</head>
<body>
<main class="canvas">
  <section class="label-wrap">
    <svg class="label-art" width="511" height="1078" viewBox="0 0 511 1078" xmlns="http://www.w3.org/2000/svg">
      <defs>
        <linearGradient id="bandShade" x1="0" y1="0" x2="1" y2="0">
          <stop offset="0" stop-color="var(--band-edge)"/>
          <stop offset="0.45" stop-color="var(--band-mid)"/>
          <stop offset="1" stop-color="var(--band-edge)"/>
        </linearGradient>
      </defs>
      <rect class="contour-pattern" x="0" y="0" width="511" height="1078" fill="var(--wrap-bg)"
            role="img" aria-label="Light blue topographic contour line pattern on white"/>
      <polygon class="colour-band" fill="url(#bandShade)"
        points="0,549 30,540 48,531 70,527 92,516 120,509 140,497 168,490 190,478 214,471 238,459 262,452 286,438 312,431 336,419 360,411 382,397 408,389 430,375 452,366 476,350 494,342 511,328
                511,648 492,660 470,672 452,680 430,696 408,704 388,720 364,728 342,744 318,752 296,766 270,774 248,788 222,796 198,810 174,816 150,830 124,836 100,848 76,854 52,864 26,870 0,880"/>
    </svg>
    <div class="label-text">
      <h1 class="brand-name">RIVO</h1>
      <p class="variant-name">BRIGHT</p>
      <ul class="ingredients">
        <li><span class="origin">US Sourced</span> Pure Epsom Salt</li>
        <li>(Magnesium Sulfate)</li>
        <li>+Fir Balsam</li>
        <li>+Abies sibirica</li>
      </ul>
      <p class="net-weight">NET WT. 3vLBS (1360g)</p>
    </div>
  </section>
</main>
</body>
</html>
```